Professional Modern Website Design

We are a premium IT services provider to the financial industry based in London. Our company is called Veltra our current holding page is www.veltra-example.co.uk. We require a new website to match our new corporate identity. This project is for the design phase only. Development will be handled in-house. I have attached examples of wire frames we have developed (although open to suggestions for improvement) Our brand document that should demonstrate current brand, inc how we communicate to potential clients and finally mostly completed web-content.
We are looking for designers that can create something that sets us apart from our competitors.
Target Market(s)
IT Decision makers in Finance companies such as; hedge funds, private investment banks etc
Industry/Entity Type
Financial
Number of Pages Required
5+ page
Requirements
Must have
- hexagon elements in the design, unique design.
Nice to have
- Blog and social media feeds
Should not have
- Should not resemble a downloaded template

```html
<!DOCTYPE html>
<html lang="en">
<head>
<meta charset="utf-8">
<title>Veltra – IT Services for Finance</title>
<link href="https://fonts.googleapis.com/css2?family=Open+Sans:wght@300;400;600;700;800&family=Open+Sans+Condensed:wght@300;700&display=swap" rel="stylesheet">
<style>
:root{
  --orange:#f36c0c;
  --orange-dark:#d95c05;
  --charcoal:#4a4a4a;
  --charcoal-deep:#3e3e3e;
  --ink:#222;
  --grey-text:#666;
  --light:#f2f2f2;
  --white:#fff;
}
*{box-sizing:border-box;margin:0;padding:0}
html,body{width:1200px;height:3243px;overflow:hidden}
body{font-family:"Open Sans",Arial,sans-serif;color:var(--ink);background:var(--white);position:relative}
section,header,footer{position:absolute;left:0;width:1200px}
.hex-label{font-weight:700;font-size:15px;text-align:center;line-height:1.25}

/* Header / hero */
.hero{top:0;height:562px;background:linear-gradient(180deg,#c9cdd1 0%,#e8eaec 40%,#9aa0a6 100%)}
.hero-photo{position:absolute;inset:0;background:
  linear-gradient(90deg,rgba(40,45,55,.55) 0%,rgba(255,255,255,.05) 35%,rgba(255,255,255,.2) 65%,rgba(40,45,55,.55) 100%)}
.nav{position:absolute;top:0;left:0;width:1200px;height:64px;background:rgba(40,40,40,.55)}
.nav a{position:absolute;top:22px;color:var(--white);text-decoration:none;font-size:15px;font-weight:600;letter-spacing:.5px}
.nav a.active{background:var(--orange);border-radius:14px;padding:3px 14px;top:19px}
.brand{position:absolute;left:520px;top:0;width:160px;height:112px;background:rgba(40,40,40,.75);display:flex;align-items:center;justify-content:center;gap:10px}
.brand-mark{width:16px;height:16px;background:var(--orange)}
.brand-name{color:var(--white);font-weight:700;font-size:24px;letter-spacing:1px}
.hero-band{position:absolute;left:290px;top:250px;width:620px;height:200px;background:rgba(30,30,30,.55);text-align:center;color:var(--white);padding-top:10px}
.hero-band h1{font-size:34px;font-weight:700;letter-spacing:2px}
.hero-band p{font-size:17px;line-height:1.4;margin:10px 20px 0}
.btn-orange{display:inline-block;margin-top:14px;background:var(--orange);color:var(--white);font-weight:700;font-size:16px;padding:9px 26px;border-radius:22px}

/* Services */
.services{top:562px;height:487px;background:var(--white)}
.section-title{text-align:center;color:var(--orange);font-weight:400;font-size:44px}
.services .section-title{margin-top:48px}
.service-grid{position:absolute;top:120px;left:145px;width:910px;display:flex;justify-content:space-between}
.service{width:170px;text-align:center}
.service svg{width:140px;height:150px}
.service .hex-label{margin-top:8px;height:40px}
.service p{font-size:11px;color:var(--grey-text);line-height:1.45;margin-top:8px}

/* Steps */
.steps{top:1049px;height:524px;background:var(--charcoal)}
.steps h2{color:var(--white);font-family:"Open Sans Condensed","Open Sans",sans-serif;font-weight:300;font-size:46px;text-align:center;margin-top:38px}
.step-line{position:absolute;top:270px;left:297px;width:606px;height:2px;background:#8a8a8a}
.step-dot{position:absolute;top:263px;width:16px;height:16px;border-radius:50%;background:var(--white)}
.step{position:absolute;top:180px;width:300px;text-align:center;color:var(--white)}
.step svg{width:170px;height:180px}
.step h3{font-size:21px;font-weight:700;margin-top:6px}
.step p{font-size:12.5px;line-height:1.5;color:#e2e2e2;margin:14px 14px 0}

/* Managed services */
.managed{top:1573px;height:314px;background:var(--white)}
.managed-photo{position:absolute;left:0;top:0;width:595px;height:314px;background:linear-gradient(120deg,#dfe6ec 0%,#b9c7d3 45%,#eef2f5 100%)}
.managed-copy{position:absolute;left:618px;top:42px;width:560px}
.managed-copy h2{color:var(--orange);font-weight:400;font-size:42px}
.managed-copy .lead{font-size:15px;line-height:1.3;margin-top:8px}
.managed-list{list-style:none;margin-top:14px}
.managed-list li{display:flex;align-items:center;gap:12px;font-size:22px;color:#8a8a8a;height:40px}
.managed-list svg{width:22px;height:22px}

/* Values */
.values{top:1887px;height:316px}
.values-panel{position:absolute;left:0;top:0;width:617px;height:316px;background:var(--orange);color:var(--white);padding:48px 0 0 160px}
.values-panel h2{font-weight:400;font-size:46px}
.values-panel p{font-size:15px;line-height:1.5;margin-top:10px;width:420px}
.btn-dark{display:inline-block;margin-top:22px;background:#111;color:var(--white);font-weight:700;font-size:15px;padding:9px 24px;border-radius:20px}
.values-photo{position:absolute;left:617px;top:0;width:583px;height:316px;background:linear-gradient(135deg,#f4f4f4 0%,#9a9a9a 50%,#3a3a3a 100%)}

/* Finance audiences */
.audiences{top:2203px;height:508px;background:var(--white)}
.audiences .section-title{margin-top:30px;font-size:44px}
.audiences .sub{text-align:center;font-size:16px;margin-top:6px}
.audience-grid{position:absolute;top:160px;left:165px;width:870px;display:flex;justify-content:space-between}
.audience{width:200px;text-align:center}
.audience svg{width:160px;height:170px}
.audience .hex-label{font-size:17px;margin-top:6px}
.audience p{font-size:11.5px;color:var(--grey-text);line-height:1.5;margin-top:10px}

/* Partners */
.partners{top:2711px;height:222px;background:var(--charcoal)}
.partners h2{color:var(--white);font-weight:400;font-size:40px;text-align:center;margin-top:40px}
.partner-row{display:flex;justify-content:center;align-items:center;gap:62px;margin-top:38px}
.partner{color:var(--white);font-weight:600;font-size:30px}
.partner-badge{display:flex;align-items:center;gap:10px}
.partner-badge span{width:30px;height:30px;background:var(--white)}

/* Footer */
.site-footer{top:2933px;height:270px;background:var(--orange);color:var(--white)}
.foot-col{position:absolute;top:56px}
.foot-col h4{font-weight:400;font-size:22px;margin-bottom:12px}
.foot-col ul{list-style:none}
.foot-col li{font-size:13px;line-height:1.55;display:flex;align-items:center;gap:8px}
.quick li{justify-content:space-between;width:100px}
.social-dot{width:14px;height:14px;border-radius:50%;background:var(--white)}
.office{font-size:12.5px;line-height:1.45}
.office strong{display:flex;align-items:center;gap:8px;font-size:14px}
.legal{position:absolute;top:3203px;left:0;width:1200px;height:40px;text-align:center;font-size:12px;color:#777;padding-top:14px}
.legal b{color:var(--orange);font-weight:400}
</style>
</head>
<body>

<header class="hero">
  <div class="hero-photo" role="img" aria-label="Photo of a data centre aisle lined with server racks"></div>
  <nav class="nav">
    <a class="active" style="left:172px">HOME</a>
    <a style="left:296px">ABOUT</a>
    <a style="left:412px">SERVICES</a>
    <a style="left:695px">PARTNERS</a>
    <a style="left:835px">CLIENTS</a>
    <a style="left:958px">CONTACT</a>
  </nav>
  <div class="brand"><span class="brand-mark"></span><span class="brand-name">Veltra</span></div>
  <div class="hero-band">
    <h1>DATA CENTRE &amp; INFRASTRUCTURE</h1>
    <p>Veltra is one of the leading systems integrators to the world's finance sector. We are an extension of your business and our services portfolio has been built so you always have access to a complete partner.</p>
    <span class="btn-orange">LEARN MORE</span>
  </div>
</header>

<section class="services">
  <h2 class="section-title">Our Services</h2>
  <div class="service-grid">
    <div class="service">
      <svg viewBox="0 0 100 108" role="img" aria-label="Illustration of server hardware"><polygon points="50,3 95,28 95,80 50,105 5,80 5,28" fill="#fff" stroke="#333" stroke-width="4"/><polygon points="50,12 87,33 87,75 50,96 13,75 13,33" fill="#d7d9dc"/><path d="M87,33 L87,75 L50,96" fill="none" stroke="var(--orange)" stroke-width="4"/></svg>
      <div class="hex-label">Data Centre &amp;<br>Infrastructure</div>
      <p>Veltra offers analysis, assessment, implementation and management of your infrastructure to boost your company's productivity and profitability.</p>
    </div>
    <div class="service">
      <svg viewBox="0 0 100 108" role="img" aria-label="Illustration of support tools"><polygon points="50,3 95,28 95,80 50,105 5,80 5,28" fill="#fff" stroke="#333" stroke-width="4"/><polygon points="50,12 87,33 87,75 50,96 13,75 13,33" fill="#d4d6d9"/><path d="M87,33 L87,75 L50,96" fill="none" stroke="var(--orange)" stroke-width="4"/></svg>
      <div class="hex-label">IT Support, Manage &amp;<br>Professional Services</div>
      <p>Veltra built its reputation on IT support, managed and professional services and it continues to operate with these as a priority.</p>
    </div>
    <div class="service">
      <svg viewBox="0 0 100 108" role="img" aria-label="Illustration of a globe and telephone"><polygon points="50,3 95,28 95,80 50,105 5,80 5,28" fill="#fff" stroke="#333" stroke-width="4"/><polygon points="50,12 87,33 87,75 50,96 13,75 13,33" fill="#cfd2d6"/><path d="M87,33 L87,75 L50,96" fill="none" stroke="var(--orange)" stroke-width="4"/></svg>
      <div class="hex-label">Voice &amp; Data<br>Networks</div>
      <p>Veltra can offer hosted voice over IP and more traditional PBX systems based around a flexible, mobile and agile platform.</p>
    </div>
    <div class="service">
      <svg viewBox="0 0 100 108" role="img" aria-label="Illustration of cloud hosting"><polygon points="50,3 95,28 95,80 50,105 5,80 5,28" fill="#fff" stroke="#333" stroke-width="4"/><polygon points="50,12 87,33 87,75 50,96 13,75 13,33" fill="#e1e3e6"/><path d="M87,33 L87,75 L50,96" fill="none" stroke="var(--orange)" stroke-width="4"/></svg>
      <div class="hex-label">HOSTING<br>&amp; CLOUD</div>
      <p>Veltra can help companies adopt a highly secure hosting and cloud solution to keep data safe and processes efficient.</p>
    </div>
    <div class="service">
      <svg viewBox="0 0 100 108" role="img" aria-label="Illustration of a security shield"><polygon points="50,3 95,28 95,80 50,105 5,80 5,28" fill="#fff" stroke="#333" stroke-width="4"/><polygon points="50,12 87,33 87,75 50,96 13,75 13,33" fill="#f08a3e"/><path d="M87,33 L87,75 L50,96" fill="none" stroke="var(--orange)" stroke-width="4"/></svg>
      <div class="hex-label">IT<br>Security &amp; IRM</div>
      <p>Veltra offers specialised information risk and IT security management. We know how important protection is to your whole organisation.</p>
    </div>
  </div>
</section>

<section class="steps">
  <h2>EASY 3 STEPS TO OBTAINING SERVICE</h2>
  <div class="step-line"></div>
  <div class="step-dot" style="left:440px"></div>
  <div class="step-dot" style="left:746px"></div>
  <div class="step" style="left:147px">
    <svg viewBox="0 0 100 108"><polygon points="50,3 95,28 95,80 50,105 5,80 5,28" fill="var(--orange)" stroke="#fff" stroke-width="3"/><rect x="33" y="32" width="30" height="40" fill="#fff"/><g stroke="var(--orange)" stroke-width="3"><line x1="38" y1="42" x2="58" y2="42"/><line x1="38" y1="50" x2="58" y2="50"/><line x1="38" y1="58" x2="52" y2="58"/></g><circle cx="64" cy="66" r="8" fill="none" stroke="#fff" stroke-width="3"/><line x1="70" y1="72" x2="77" y2="79" stroke="#fff" stroke-width="4"/></svg>
    <h3>Analysis &amp; Assessment</h3>
    <p>We will analyse your current infrastructure and assess what you need to help your business grow. We can offer advice on both on and off premise solutions to meet compliance and your enterprise's objectives.</p>
  </div>
  <div class="step" style="left:450px">
    <svg viewBox="0 0 100 108"><polygon points="50,3 95,28 95,80 50,105 5,80 5,28" fill="var(--orange)" stroke="#fff" stroke-width="3"/><circle cx="50" cy="54" r="17" fill="none" stroke="#fff" stroke-width="9" stroke-dasharray="7 4"/><circle cx="50" cy="54" r="9" fill="#fff"/><circle cx="50" cy="54" r="4" fill="var(--orange)"/></svg>
    <h3>Implementation</h3>
    <p>We will implement the best solutions for you and ensure everything you need is set up without a gap in service. If you need to migrate applications or services, we will ensure it runs smoothly and all risks are addressed ahead of time.</p>
  </div>
  <div class="step" style="left:753px">
    <svg viewBox="0 0 100 108"><polygon points="50,3 95,28 95,80 50,105 5,80 5,28" fill="var(--orange)" stroke="#fff" stroke-width="3"/><rect x="30" y="58" width="9" height="16" fill="#fff"/><rect x="43" y="48" width="9" height="26" fill="#fff"/><rect x="56" y="38" width="9" height="36" fill="#fff"/><polyline points="28,52 46,38 58,30 70,24" fill="none" stroke="#fff" stroke-width="3"/><polygon points="72,20 74,30 64,26" fill="#fff"/></svg>
    <h3>Adapt and Grow</h3>
    <p>We will analyse your current infrastructure and assess what you need to help your business grow. We can offer advice on both on and off premise solutions to meet compliance and your enterprise's objectives.</p>
  </div>
</section>

<section class="managed">
  <div class="managed-photo" role="img" aria-label="Photo of a smiling consultant in a bright office"></div>
  <div class="managed-copy">
    <h2>Managed Services</h2>
    <p class="lead">We Merge the <b>Best Products</b> with <b>Top-Class Maintenance Services</b> to Ensure our Integration Meets Your Objectives.</p>
    <ul class="managed-list">
      <li><svg viewBox="0 0 22 22"><circle cx="11" cy="11" r="9" fill="none" stroke="var(--orange)" stroke-width="2"/><polyline points="9,6 14,11 9,16" fill="none" stroke="var(--orange)" stroke-width="2"/></svg>IRM CONSULTATION SERVICES</li>
      <li><svg viewBox="0 0 22 22"><circle cx="11" cy="11" r="9" fill="none" stroke="var(--orange)" stroke-width="2"/><polyline points="9,6 14,11 9,16" fill="none" stroke="var(--orange)" stroke-width="2"/></svg>CLOUD-BASED MANAGED SERVICES</li>
      <li><svg viewBox="0 0 22 22"><circle cx="11" cy="11" r="9" fill="none" stroke="var(--orange)" stroke-width="2"/><polyline points="9,6 14,11 9,16" fill="none" stroke="var(--orange)" stroke-width="2"/></svg>VOICE &amp; DATA NETWORKS SERVICES</li>
    </ul>
  </div>
</section>

<section class="values">
  <div class="values-panel">
    <h2>Our Values</h2>
    <p>Our objective is to provide true business value to our clients, enabling them to achieve their desired goals and initiatives. To do this all our people and our partners are aligned across our three core values.</p>
    <span class="btn-dark">READ MORE</span>
  </div>
  <div class="values-photo" role="img" aria-label="Black and white photo of a hand writing beside a laptop"></div>
</section>

<section class="audiences">
  <h2 class="section-title">If You're Part of a Financial Organisation</h2>
  <p class="sub">We have the power to help everyone work more efficiently, productively and profitably.</p>
  <div class="audience-grid">
    <div class="audience">
      <svg viewBox="0 0 100 108" role="img" aria-label="Portrait of a chief executive officer"><polygon points="50,3 95,28 95,80 50,105 5,80 5,28" fill="#fff" stroke="#bdbdbd" stroke-width="3"/><polygon points="50,11 88,32 88,76 50,97 12,76 12,32" fill="#cfcfcf"/></svg>
      <div class="hex-label">Chief Executive Officer</div>
      <p>You need to develop and implement strategies for business growth, while ensuring profitability. You're aware your biggest asset is your staff and a happy workforce is a productive one.</p>
    </div>
    <div class="audience">
      <svg viewBox="0 0 100 108" role="img" aria-label="Portrait of a chief financial officer"><polygon points="50,3 95,28 95,80 50,105 5,80 5,28" fill="#fff" stroke="#bdbdbd" stroke-width="3"/><polygon points="50,11 88,32 88,76 50,97 12,76 12,32" fill="#c6c6c6"/></svg>
      <div class="hex-label">Chief Financial Officer</div>
      <p>Your key responsibility is to obtain the maximum ROI from products and services. You understand investment opportunities, providing they return higher efficiencies and revenues.</p>
    </div>
    <div class="audience">
      <svg viewBox="0 0 100 108" role="img" aria-label="Portrait of an IT manager"><polygon points="50,3 95,28 95,80 50,105 5,80 5,28" fill="#fff" stroke="#bdbdbd" stroke-width="3"/><polygon points="50,11 88,32 88,76 50,97 12,76 12,32" fill="#d3d3d3"/></svg>
      <div class="hex-label">IT Manager/CTO</div>
      <p>Integration with partners and services is your key concern. You want to make sure any IT system you implement will work with the whole infrastructure of your company.</p>
    </div>
    <div class="audience">
      <svg viewBox="0 0 100 108" role="img" aria-label="Group photo of employees"><polygon points="50,3 95,28 95,80 50,105 5,80 5,28" fill="#fff" stroke="#bdbdbd" stroke-width="3"/><polygon points="50,11 88,32 88,76 50,97 12,76 12,32" fill="#d8c4b4"/></svg>
      <div class="hex-label">Employees</div>
      <p>You're working hard but not getting anywhere fast. You want the tools to make your job easier so you can spend more time thinking about what you're doing rather than how you're doing it.</p>
    </div>
  </div>
</section>

<section class="partners">
  <h2>Our Partners</h2>
  <div class="partner-row">
    <span class="partner partner-badge"><span></span>Northgrid</span>
    <span class="partner">Cirrolane</span>
    <span class="partner">Brightstore</span>
    <span class="partner">Vantix</span>
    <span class="partner">Helio</span>
  </div>
</section>

<footer class="site-footer">
  <div class="foot-col quick" style="left:168px">
    <h4>Quick Links</h4>
    <ul><li>Home<span>›</span></li><li>About<span>›</span></li><li>Services<span>›</span></li><li>Partners<span>›</span></li><li>Clients<span>›</span></li><li>Contact<span>›</span></li></ul>
  </div>
  <div class="foot-col" style="left:381px">
    <h4>Follow Us</h4>
    <ul><li><span class="social-dot"></span>Friendwall</li><li><span class="social-dot"></span>Chirper</li><li><span class="social-dot"></span>Worklink</li><li><span class="social-dot"></span>Blog</li></ul>
  </div>
  <div class="foot-col" style="left:581px">
    <h4>Contact Us</h4>
    <div class="office"><strong><svg width="12" height="16" viewBox="0 0 12 16"><path d="M6 0a6 6 0 0 1 6 6c0 4-6 10-6 10S0 10 0 6a6 6 0 0 1 6-6z" fill="#fff"/><circle cx="6" cy="6" r="2" fill="var(--orange)"/></svg>London Office</strong>48 HARROWGATE LANE,<br>LONDON EC9 4ZX<br>t: +44 (0)20 0000 1234<br>e: info@veltra-example.co.uk</div>
  </div>
  <div class="foot-col" style="left:811px">
    <h4>&nbsp;</h4>
    <div class="office"><strong><svg width="12" height="16" viewBox="0 0 12 16"><path d="M6 0a6 6 0 0 1 6 6c0 4-6 10-6 10S0 10 0 6a6 6 0 0 1 6-6z" fill="#fff"/><circle cx="6" cy="6" r="2" fill="var(--orange)"/></svg>Essex Office</strong>7 MILL COURT, KESTREL ROAD<br>WESTBROOK, ESSEX SS0 9QT<br>Support: +44 (0)20 0000 1235<br>e: info@veltra-example.co.uk</div>
  </div>
</footer>
<div class="legal">Copyright © 2013 <b>VELTRA LIMITED</b>. All Rights Reserved</div>

</body>
</html>
```